Create Vintage poster for wine festival

Vintage poster, lots of colour, for a one off event :- Spanish theme; more Kesten/Tolvandu than pictures of Bulls & bullfighters. Check out old Spanish posters around the 1930's

Information on poster

Event :- Global Quince Night 26th May 2013
Korelume 2pm - 6pm
14 Harrowgate lane, Sydney 2000
Ph 8135 -6470 www.korelume.com.au

Industry/Entity Type

Festival

Requirements
Must have
• lots of colour, and description of event.

Ideal font to be used would be similar to our current logo, which can be found at the bottom of the page
http://www.korelume.com.au/Bookings.html

```html
<!DOCTYPE html>
<html lang="en">
<head>
<meta charset="utf-8">
<title>Korelume – Global Quince Night</title>
<link rel="stylesheet" href="https://fonts.googleapis.com/css2?family=Almendra:wght@700&display=swap">
<style>
  :root {
    --poster-orange: #f29a1e;
    --poster-orange-light: #f7b24a;
    --frame-black: #111111;
    --panel-cream: #fcf9e4;
    --tile-yellow: #f4e21c;
    --tile-peach: #f4a86a;
    --tile-lilac: #9d8bb0;
    --tile-green: #a6cf8a;
    --grape-brown: #5b4c45;
    --ornament-red: #b52a2e;
    --brand-red: #a31f24;
    --bar-red: #a31f22;
    --bar-orange: #f0961e;
    --bar-wine: #8a0034;
    --bar-olive: #7a9a3b;
    --bar-plum: #7a2449;
    --text-light: #ffffff;
  }
  html, body {
    margin: 0;
    padding: 0;
    width: 900px;
    height: 1200px;
    overflow: hidden;
  }
  .poster {
    position: relative;
    width: 900px;
    height: 1200px;
    background: radial-gradient(ellipse at center, var(--poster-orange-light) 0%, var(--poster-orange) 75%);
    font-family: "Almendra", Georgia, serif;
    font-weight: 700;
  }
  .tile-border {
    position: absolute;
    left: 50px;
    top: 50px;
    width: 790px;
    height: 1088px;
    border: 5px solid var(--frame-black);
    background:
      linear-gradient(135deg, var(--tile-peach) 0%, var(--tile-yellow) 25%, var(--tile-lilac) 50%, var(--tile-yellow) 75%, var(--tile-green) 100%);
  }
  .content-panel {
    position: absolute;
    left: 170px;
    top: 170px;
    width: 556px;
    height: 856px;
    border: 3px solid var(--frame-black);
    background: var(--panel-cream);
  }
  .grapes {
    position: absolute;
    top: 8px;
    height: 60px;
    width: 170px;
    border-radius: 0 0 40px 40px;
    background: linear-gradient(180deg, var(--grape-brown), rgba(91, 76, 69, 0.35));
    opacity: 0.75;
  }
  .grapes--left { left: 4px; }
  .grapes--right { right: 0; }
  .brand-crest {
    position: absolute;
    left: 24px;
    top: 72px;
    width: 508px;
    height: 260px;
    border-radius: 50%;
    background: radial-gradient(ellipse at center, rgba(181, 42, 46, 0.22) 0%, rgba(181, 42, 46, 0.08) 60%, rgba(181, 42, 46, 0) 75%);
  }
  .brand-name {
    position: absolute;
    left: 0;
    top: 168px;
    width: 556px;
    margin: 0;
    text-align: center;
    font-size: 56px;
    line-height: 70px;
    color: var(--brand-red);
  }
  .event-label {
    position: absolute;
    left: 0;
    top: 370px;
    width: 556px;
    margin: 0;
    text-align: center;
    font-size: 28px;
    line-height: 40px;
    color: var(--brand-red);
  }
  .event-details {
    position: absolute;
    left: 11px;
    top: 420px;
    width: 532px;
    margin: 0;
    padding: 0;
    list-style: none;
  }
  .event-details li {
    height: 52px;
    margin-bottom: 18.5px;
    line-height: 52px;
    text-align: center;
    font-size: 30px;
    color: var(--text-light);
  }
  .event-details .detail--title { background: var(--bar-red); }
  .event-details .detail--date { background: var(--bar-orange); }
  .event-details .detail--time { background: var(--bar-wine); }
  .event-details .detail--address { background: var(--bar-olive); }
  .event-details .detail--phone { background: var(--bar-plum); }
  .event-details .detail--web { background: var(--bar-red); font-size: 27px; }
</style>
</head>
<body>
  <main class="poster">
    <div class="tile-border" role="img" aria-label="Stained-glass tile border in yellow, peach, lilac and green"></div>
    <section class="content-panel">
      <div class="grapes grapes--left" role="img" aria-label="Hanging grape clusters"></div>
      <div class="grapes grapes--right" role="img" aria-label="Hanging grape clusters"></div>
      <div class="brand-crest" role="img" aria-label="Red scrollwork flourish around the venue name"></div>
      <h1 class="brand-name">Korelume</h1>
      <p class="event-label">Event :-</p>
      <ul class="event-details">
        <li class="detail--title">Global Quince Night</li>
        <li class="detail--date">26th May 2013</li>
        <li class="detail--time">Korelume 2pm - 6pm</li>
        <li class="detail--address">14 Harrowgate lane, Sydney 2000</li>
        <li class="detail--phone">Ph: 8135 -6470</li>
        <li class="detail--web">www.korelume.com.au</li>
      </ul>
    </section>
  </main>
</body>
</html>
```